Business card and stationary designs for Harbor Summit Mentor
Harbor Summit Mentor
Business card and stationary designs for Harbor Summit Mentor - Consulting
Creative Brief
Professional
Reed Calloway
Executive & Professional Coach
4187 Willow Bend Lane Dallas TX 75231
RCalloway@harborsummitmentor.example
www.HarborSummitMentor.example
I want this to look clean, cutting edge, and for the design to stand out.
On the back of the business card I would like my logo and the phrase "Executive & Professional Coaching"

```html
<!DOCTYPE html>
<html lang="en">
<head>
<meta charset="utf-8">
<title>Harbor Summit Mentor – Stationery</title>
<link rel="stylesheet" href="https://fonts.googleapis.com/css2?family=Cinzel:wght@400&family=Lato:wght@400;700&display=swap">
<style>
:root{
  --backdrop:#ececec;
  --paper:#ffffff;
  --ink:#2b2b2b;
  --ink-soft:#6b6b6b;
  --band:#3a3a3a;
  --band-text:#e6e6e6;
  --pattern-a:#f7f7f7;
  --pattern-b:#dcdcdc;
  --rule:#cfcfcf;
}
*{box-sizing:border-box;margin:0;padding:0}
html,body{width:1200px;height:936px;overflow:hidden;background:var(--backdrop)}
body{position:relative;font-family:'Lato',sans-serif;color:var(--ink)}
.sheet{position:absolute;background:var(--paper);box-shadow:0 2px 8px rgba(0,0,0,.14);overflow:hidden}
.brand{font-family:'Cinzel',serif;font-weight:400;color:var(--ink);display:flex;align-items:center;gap:8px;letter-spacing:.04em;white-space:nowrap}
.brand .mark{display:inline-block;background:var(--ink)}
.pattern{position:absolute;left:0;right:0;background:linear-gradient(180deg,var(--pattern-a),var(--pattern-b))}
.band{position:absolute;left:0;right:0;background:var(--band);color:var(--band-text);display:flex;align-items:center;justify-content:center}
.site{font-family:'Lato',sans-serif;letter-spacing:.22em;color:var(--ink);text-align:center}

/* Letterhead */
.letterhead{left:25px;top:13px;width:470px;height:557px}
.letterhead .brand{position:absolute;left:0;right:0;top:34px;justify-content:center;font-size:18px}
.letterhead .brand .mark{width:9px;height:9px}
.letter{position:absolute;left:48px;right:48px;top:110px;font-size:5.6px;line-height:1.55;color:var(--ink-soft)}
.letter p{margin-bottom:7px}
.letter .signature{width:34px;height:12px;background:linear-gradient(90deg,#bdbdbd,#e6e6e6);margin:4px 0 6px}
.letter .signer{color:var(--ink)}
.letterhead .site{position:absolute;left:0;right:0;top:447px;font-size:9px}
.letterhead .pattern{top:462px;height:74px}
.letterhead .band{bottom:8px;height:13px;font-size:5px;letter-spacing:.06em;gap:14px}

/* Cover sheet */
.cover{left:540px;top:13px;width:636px;height:557px}
.cover .brand{position:absolute;left:0;right:0;top:184px;justify-content:center;font-size:30px}
.cover .brand .mark{width:14px;height:14px}
.cover .tag{position:absolute;left:0;right:0;top:226px;text-align:center;font-size:9px;letter-spacing:.3em;color:var(--ink-soft)}
.cover .pattern{top:405px;height:112px}
.cover .band{bottom:22px;height:17px;font-size:8px;letter-spacing:.22em}

/* Business cards */
.card{width:216px;height:107px;left:25px}
.card-front{top:653px}
.card-front .brand{position:absolute;left:12px;top:12px;font-size:10px;gap:5px}
.card-front .brand .mark{width:6px;height:6px}
.card-front .person{position:absolute;left:12px;top:44px;font-size:6px;line-height:1.5}
.card-front .person strong{font-size:7px}
.card-front .band{bottom:0;height:22px;font-size:4.6px;justify-content:flex-start;padding-left:12px;flex-direction:column;align-items:flex-start;line-height:1.4}
.card-back{top:772px}
.card-back .brand{position:absolute;left:0;right:0;top:28px;justify-content:center;font-size:12px;gap:6px}
.card-back .brand .mark{width:7px;height:7px}
.card-back .band{bottom:0;height:26px;font-size:7px;letter-spacing:.08em}

/* Envelope front */
.envelope-front{left:266px;top:653px;width:455px;height:220px}
.envelope-front .brand{position:absolute;left:24px;top:24px;font-size:14px;gap:6px}
.envelope-front .brand .mark{width:8px;height:8px}
.envelope-front .address{position:absolute;left:24px;top:50px;font-size:6px;color:var(--ink-soft)}
.envelope-front .band{bottom:0;height:20px;font-size:7px;letter-spacing:.22em}

/* Envelope back */
.envelope-back{left:746px;top:653px;width:430px;height:220px}
.envelope-back .site{position:absolute;left:0;right:0;top:30px;font-size:9px}
.envelope-back svg{position:absolute;left:0;top:0}
</style>
</head>
<body>

<section class="sheet letterhead">
  <div class="brand"><span class="mark"></span>Harbor Summit Mentor</div>
  <div class="letter">
    <p>May 6, 2025</p>
    <p>Dear Client,</p>
    <p>Thank you for meeting with me last week. It was a pleasure to learn about your goals for the coming year and the growth you hope to see across your leadership team. I look forward to building a plan that fits your people and your pace.</p>
    <p>Our sessions will focus on clear goals, honest feedback and steady habits that help each leader serve others well.</p>
    <p>Please reach out at any time with questions. I am glad to help you and your team move forward with confidence and purpose.</p>
    <p>Best Regards,</p>
    <div class="signature" role="img" aria-label="Handwritten signature"></div>
    <p class="signer">Reed Calloway<br>Executive &amp; Professional Coach</p>
  </div>
  <div class="site">www.HarborSummitMentor.example</div>
  <div class="pattern" role="img" aria-label="Faint decorative pattern band"></div>
  <div class="band"><span>4187 Willow Bend Lane Dallas TX 75231</span><span>RCalloway@harborsummitmentor.example</span></div>
</section>

<section class="sheet cover">
  <div class="brand"><span class="mark"></span>Harbor Summit Mentor</div>
  <div class="tag">EXECUTIVE &amp; PROFESSIONAL COACHING</div>
  <div class="pattern" role="img" aria-label="Faint decorative pattern band"></div>
  <div class="band">www.HarborSummitMentor.example</div>
</section>

<section class="sheet card card-front">
  <div class="brand"><span class="mark"></span>Harbor Summit Mentor</div>
  <div class="person"><strong>Reed Calloway</strong><br>Executive &amp; Professional Coach</div>
  <div class="band"><span>4187 Willow Bend Lane Dallas TX 75231</span><span>RCalloway@harborsummitmentor.example</span></div>
</section>

<section class="sheet card card-back">
  <div class="brand"><span class="mark"></span>Harbor Summit Mentor</div>
  <div class="band">Executive &amp; Professional Coaching</div>
</section>

<section class="sheet envelope-front">
  <div class="brand"><span class="mark"></span>Harbor Summit Mentor</div>
  <div class="address">4187 Willow Bend Lane Dallas TX 75231</div>
  <div class="band">www.HarborSummitMentor.example</div>
</section>

<section class="sheet envelope-back">
  <div class="site">www.HarborSummitMentor.example</div>
  <svg width="430" height="220" viewBox="0 0 430 220" aria-hidden="true">
    <polyline points="0,70 215,150 430,70" fill="none" stroke="var(--rule)" stroke-width="1"/>
    <line x1="0" y1="220" x2="170" y2="135" stroke="var(--rule)" stroke-width="1"/>
    <line x1="430" y1="220" x2="260" y2="135" stroke="var(--rule)" stroke-width="1"/>
  </svg>
</section>

</body>
</html>
```